Fitness Coach Needs Book Cover Created

I would like a book cover created for my upcoming project titled,
Steady Stride After Forty: 9 Quiet Rituals for a Brighter Routine

Target Market(s)

Men & Women 30-40 years old

Industry/Entity Type

Fitness

Font styles to use
Serif

Requirements
Must have
• 3 color cover. I have attached my name to be used at bottom of cover and uploaded a couple sample covers as well.
Should not have
• stock imaging.

```html
<!DOCTYPE html>
<html lang="en">
<head>
<meta charset="utf-8">
<title>Steady Stride After Forty — Book Cover</title>
<link rel="stylesheet" href="https://fonts.googleapis.com/css2?family=Bebas+Neue&family=Montserrat:wght@400;800&display=swap">
<style>
  :root {
    --teal-edge: #4fa9a3;
    --teal-mid: #7cc6bd;
    --teal-glow: #a4ddd4;
    --gold-edge: #f0a31a;
    --gold-mid: #f5c43a;
    --gold-glow: #f8de6a;
    --ink: #1c1c1c;
    --ink-soft: #2a2a2a;
  }
  html, body {
    margin: 0;
    padding: 0;
    width: 815px;
    height: 1200px;
    overflow: hidden;
    background: #ffffff;
  }
  .cover {
    position: relative;
    width: 815px;
    height: 1200px;
    overflow: hidden;
  }
  .cover__sky {
    position: absolute;
    left: 0; top: 0;
    width: 815px; height: 763px;
    background:
      radial-gradient(ellipse 70% 55% at 45% 75%, var(--teal-glow) 0%, rgba(164,221,212,0) 70%),
      linear-gradient(180deg, var(--teal-edge) 0%, var(--teal-mid) 45%, var(--teal-glow) 100%);
  }
  .cover__ground {
    position: absolute;
    left: 0; top: 763px;
    width: 815px; height: 437px;
    background:
      radial-gradient(ellipse 65% 60% at 50% 30%, var(--gold-glow) 0%, rgba(248,222,106,0) 75%),
      linear-gradient(180deg, var(--gold-mid) 0%, var(--gold-edge) 100%);
  }
  .cover__title {
    position: absolute;
    left: 0; top: 112px;
    width: 815px;
    margin: 0;
    text-align: center;
    font-family: "Bebas Neue", "Oswald", sans-serif;
    font-weight: 400;
    font-size: 138px;
    line-height: 113px;
    letter-spacing: 3px;
    color: var(--ink);
  }
  .cover__title span { display: block; }
  .cover__subtitle {
    position: absolute;
    left: 0; top: 494px;
    width: 815px;
    margin: 0;
    text-align: center;
    font-family: "Montserrat", "Helvetica Neue", sans-serif;
    font-weight: 400;
    font-size: 25px;
    line-height: 45px;
    letter-spacing: 8px;
    color: var(--ink-soft);
  }
  .cover__subtitle span { display: block; }
  .cover__emblem {
    position: absolute;
    left: 345px; top: 655px;
    width: 125px; height: 195px;
    border-radius: 40%;
    background: radial-gradient(ellipse at 50% 50%, rgba(110,140,110,0.55) 0%, rgba(150,170,110,0.25) 55%, rgba(150,170,110,0) 75%);
  }
  .cover__author {
    position: absolute;
    left: 0; top: 1050px;
    width: 815px;
    margin: 0;
    text-align: center;
    font-family: "Montserrat", "Helvetica Neue", sans-serif;
    font-weight: 800;
    font-size: 50px;
    letter-spacing: 1px;
    color: var(--ink);
  }
</style>
</head>
<body>
  <main class="cover">
    <div class="cover__sky"></div>
    <div class="cover__ground"></div>

    <h1 class="cover__title">
      <span>Steady</span>
      <span>Stride After</span>
      <span>Forty</span>
    </h1>

    <p class="cover__subtitle">
      <span>9 QUIET RITUALS</span>
      <span>FOR A BRIGHTER ROUTINE</span>
    </p>

    <div class="cover__emblem" role="img" aria-label="Glassy throwing-star emblem standing on the line between the teal and gold halves"></div>

    <p class="cover__author">RAFE OKONSKI</p>
  </main>
</body>
</html>
```